Building Certification Company needs a professional letterhead and report template

We are a modern company within an ageing industry. Our industry is responsible for life safety aspects of the built environment, we ensure buildings are safe and fit for occupation.

We use letterhead and reports everyday, we need a smart and professional letterhead that reflects the serious nature of the work we do. We also require a report template of the same ilk.

Target Market(s)

Our target market will consist mainly of professional architects, developers and construction companies.

Industry/Entity Type

Industry

Requirements
Must have
• The letterhead must have:-
Our logo
Our company details, including address, website, email, phone

Address - Suite 208 / 45 Harwick Lane Dunmore NSW 2100

Website - www.quillstonecompliance.example.au

Email - info@qsc.example.au

Phone - 02 5550 3846

The report template must have:-
A title page, which is to incorporate our logo or an aspect of our logo, get creative people.

```html
<!DOCTYPE html>
<html lang="en">
<head>
<meta charset="utf-8">
<title>Quillstone Compliance — Letterhead</title>
<link href="https://fonts.googleapis.com/css2?family=Montserrat:wght@500;600;700&display=swap" rel="stylesheet">
<style>
  :root {
    --paper: #ffffff;
    --navy: #1f3a5c;
    --ink: #1a1a1a;
    --accent: #4a7fa8;
    --tone-light: #d6e6f2;
    --tone-mid: #8fb6d6;
  }
  * { margin: 0; padding: 0; box-sizing: border-box; }
  html, body {
    width: 814px;
    height: 1200px;
    overflow: hidden;
    background: var(--paper);
  }
  .letterhead {
    position: relative;
    width: 814px;
    height: 1200px;
    background: var(--paper);
    font-family: "Montserrat", Arial, sans-serif;
  }
  .brand {
    position: absolute;
    left: 10px;
    top: 8px;
    display: flex;
    flex-direction: column;
    align-items: flex-start;
    gap: 8px;
  }
  .brand-mark {
    width: 60px;
    height: 60px;
    background: var(--accent);
    margin-left: 22px;
  }
  .brand-name {
    font-weight: 700;
    font-size: 16px;
    line-height: 1.15;
    color: var(--navy);
    letter-spacing: 0.5px;
    width: 130px;
  }
  .contact-details {
    position: absolute;
    right: 100px;
    top: 1060px;
    text-align: right;
    font-style: normal;
    font-size: 9.5px;
    font-weight: 600;
    line-height: 1.6;
    color: var(--ink);
  }
  .building-art {
    position: absolute;
    left: 722px;
    top: 880px;
    width: 92px;
    height: 320px;
    background: linear-gradient(180deg, var(--tone-light) 0%, var(--tone-mid) 100%);
  }
</style>
</head>
<body>
  <main class="letterhead">
    <header class="brand">
      <span class="brand-mark"></span>
      <span class="brand-name">Quillstone Compliance</span>
    </header>

    <address class="contact-details">
      Suite 208 / 45 Harwick Lane Dunmore NSW 2100<br>
      www.quillstonecompliance.example.au<br>
      Email - info@qsc.example.au<br>
      Phone - 02 5550 3846
    </address>

    <div class="building-art" role="img" aria-label="Illustration of modern glass office towers with trees"></div>
  </main>
</body>
</html>
```